Willowmere Cremations Business Cards

To create a business card for my company Willowmere Cremations. Remember it is a cremation company.
We want to make sure people have a business card and information. Something modern, professional
100% Online
Prices starting at $695 all-inclusive (prices subject to change without notice).
A business card is the first point of contact with the prospective client.

Contact Information for Business Card

(305) 472-8163
www.WillowmereCremationsMiami.example
willowmerecremations@mailbox.example

Requirements
Must have
• 100% Online
Prices starting at $695 all-inclusive (prices subject to change without notice)

(305) 472-8163

Must match logo style
Should not have
• No black backgrounds. Please only use the white, orange and blue from the logo

```html
<!DOCTYPE html>
<html lang="en">
<head>
<meta charset="utf-8">
<title>Willowmere Cremations Business Cards</title>
<link rel="stylesheet" href="https://fonts.googleapis.com/css2?family=Montserrat:wght@600;700&family=Lato:wght@400;700&display=swap">
<style>
  :root {
    --backdrop: #d3d3ce;
    --brand-blue: #0aa0dc;
    --brand-orange: #f7901e;
    --card-white: #ffffff;
    --ink-grey: #555b60;
  }
  * { box-sizing: border-box; margin: 0; padding: 0; }
  html, body { width: 1200px; height: 801px; overflow: hidden; }
  body { background: var(--backdrop); position: relative; font-family: "Lato", sans-serif; }

  .card {
    position: absolute;
    width: 560px;
    height: 320px;
    border-radius: 3px;
    box-shadow: 0 10px 24px rgba(0,0,0,0.18);
    overflow: hidden;
  }
  .card--front { left: 30px; top: 120px; background: var(--card-white); }
  .card--back { left: 610px; top: 360px; background: var(--brand-blue); }

  .brand {
    display: flex;
    align-items: center;
    gap: 10px;
    font-family: "Montserrat", sans-serif;
    font-weight: 700;
    line-height: 1.1;
  }
  .brand__dot { border-radius: 50%; background: var(--brand-orange); flex: none; }

  .card--front .brand {
    position: absolute;
    left: 34px;
    top: 100px;
    width: 200px;
    color: var(--brand-blue);
    font-size: 20px;
  }
  .card--front .brand__dot { width: 40px; height: 40px; }

  .divider {
    position: absolute;
    left: 250px;
    top: 70px;
    width: 1.5px;
    height: 120px;
    background: var(--brand-orange);
  }

  .contact { position: absolute; left: 268px; top: 66px; right: 14px; }
  .contact__name {
    font-family: "Montserrat", sans-serif;
    font-weight: 700;
    font-size: 25px;
    color: var(--brand-blue);
    letter-spacing: 0.3px;
  }
  .contact__title { font-size: 14px; color: var(--ink-grey); margin-top: 2px; margin-bottom: 14px; }
  .contact__line {
    display: flex;
    align-items: center;
    gap: 8px;
    font-size: 12px;
    color: var(--ink-grey);
    margin-bottom: 6px;
    white-space: nowrap;
  }
  .contact__icon { width: 12px; height: 12px; flex: none; }

  .price-band {
    position: absolute;
    left: 0;
    right: 0;
    bottom: 16px;
    height: 36px;
    background: var(--brand-blue);
    color: var(--card-white);
    font-size: 12.5px;
    display: flex;
    align-items: center;
    justify-content: center;
    letter-spacing: 0.2px;
  }

  .card--back .brand {
    position: absolute;
    left: 0;
    right: 0;
    top: 0;
    bottom: 0;
    justify-content: center;
    color: var(--card-white);
    font-size: 30px;
    gap: 16px;
  }
  .card--back .brand__dot { width: 64px; height: 64px; }
</style>
</head>
<body>

  <section class="card card--front" aria-label="Business card front">
    <div class="brand">
      <span class="brand__dot"></span>
      <span class="brand__name">Willowmere Cremations</span>
    </div>

    <div class="divider"></div>

    <div class="contact">
      <h1 class="contact__name">DANIEL REYES</h1>
      <p class="contact__title">Founder &amp; CEO</p>
      <p class="contact__line">
        <svg class="contact__icon" viewBox="0 0 24 24" aria-hidden="true"><path fill="#f7901e" d="M6.6 10.8a15.1 15.1 0 0 0 6.6 6.6l2.2-2.2c.3-.3.7-.4 1-.2 1.1.4 2.3.6 3.6.6.6 0 1 .4 1 1V20c0 .6-.4 1-1 1A17 17 0 0 1 3 4c0-.6.4-1 1-1h3.5c.6 0 1 .4 1 1 0 1.3.2 2.5.6 3.6.1.3 0 .7-.2 1z"/></svg>
        (305) 472-8163
      </p>
      <p class="contact__line">
        <svg class="contact__icon" viewBox="0 0 24 24" aria-hidden="true"><rect x="2" y="5" width="20" height="14" rx="1.5" fill="#f7901e"/><path d="M3 6l9 7 9-7" fill="none" stroke="#fff" stroke-width="1.6"/></svg>
        willowmerecremations@mailbox.example
      </p>
      <p class="contact__line">
        <svg class="contact__icon" viewBox="0 0 24 24" aria-hidden="true"><circle cx="12" cy="12" r="10" fill="#f7901e"/><path d="M2 12h20M12 2c3 3 3 17 0 20M12 2c-3 3-3 17 0 20" fill="none" stroke="#fff" stroke-width="1.3"/></svg>
        www.WillowmereCremationsMiami.example
      </p>
    </div>

    <div class="price-band">Prices starting at $695 all-inclusive (prices subject to change without notice)</div>
  </section>

  <section class="card card--back" aria-label="Business card back">
    <div class="brand">
      <span class="brand__dot"></span>
      <span class="brand__name">Willowmere Cremations</span>
    </div>
  </section>

</body>
</html>
```